Financial Services Consultant needs a business card

We need a business card for a new consulting company based in Melbourne called
"Korvane Metrics". Tagline is Measure, Monitor, Save
We would like to see business card designs that are in line with the minimal style of the website www.korvane-metrics-example.com
The font I have used on the website is Proxima Nova and would like the same or similar font used on the business card with a minimal design in line with the website Two sided with "KORVANE METRICS" MEASURE, MONITOR, SAVE on one side and name, title and contact details on the otther
Updates

Hi All, thanks for your submissions, much appreciated.

I have recently added some colour to my webiste, it is hex #3a7b74 for those that wish to use it
Thanks

Hi all

thanks very much for your design submissions I am very impressed and they are much appreciated.

Interms of general feedback please find below;

Colour: I am trying to stick to a minimal design and colour scheme for my website which is still under construction, up to 3 colours( www.korvane-metrics-example.com) it is currently black and white with a small amount of blue/green but I am open to suggestion/interpretations for a consulting company.

Card: I dont mind if it has rounded edges or straight, I was thinking about using a letterpress card if possible

Detail: the detail on the card will include; Name, Title, Mobile, Personal Email, Business Email,Web,Business Address

Once again thanks for submissions

Industry/Entity Type

Business

```html
<!DOCTYPE html>
<html lang="en">
<head>
<meta charset="utf-8">
<title>Korvane Metrics – Business Card</title>
<link rel="stylesheet" href="https://fonts.googleapis.com/css2?family=Montserrat:wght@400;500;600;700&display=swap">
<style>
  :root {
    --teal: #3a7b74;
    --teal-deep: #2c5f58;
    --teal-dark: #1f403c;
    --teal-light: #5cc1b0;
    --ink: #4a4a4a;
    --paper: #ffffff;
    --backdrop: #ececec;
  }
  * { box-sizing: border-box; margin: 0; padding: 0; }
  html, body {
    width: 1200px; height: 900px; overflow: hidden;
    background: var(--backdrop);
    font-family: "Montserrat", Arial, sans-serif;
  }
  .canvas {
    position: relative; width: 1200px; height: 900px;
  }
  .card {
    position: absolute; left: 240px; width: 720px; height: 411px;
    overflow: hidden;
    box-shadow: 0 6px 18px rgba(0,0,0,0.18);
  }
  .card-front { top: 28px; background: linear-gradient(135deg, var(--teal) 0%, var(--teal-deep) 100%); }
  .card-back { top: 466px; background: var(--paper); }

  .card-bands { position: absolute; left: 0; bottom: 0; width: 720px; height: 411px; }

  /* Front */
  .front-brand {
    position: absolute; left: 0; right: 0; top: 132px; text-align: center;
    color: var(--paper);
  }
  .front-name {
    font-weight: 700; font-size: 50px; letter-spacing: 1px; line-height: 1;
  }
  .front-tagline {
    margin-top: 14px; font-weight: 600; font-size: 19px; letter-spacing: 5px;
    text-transform: uppercase;
  }

  /* Back */
  .back-brand {
    position: absolute; left: 56px; top: 150px;
    color: var(--teal); font-weight: 700; font-size: 25px; letter-spacing: 0.5px;
  }
  .back-person {
    position: absolute; left: 408px; top: 50px;
    border-left: 3px solid var(--teal); padding-left: 12px;
  }
  .person-name { color: var(--teal); font-size: 23px; font-weight: 500; line-height: 1.1; letter-spacing: 0.5px; }
  .person-title { color: var(--ink); font-size: 13px; font-weight: 500; letter-spacing: 0.5px; margin-top: 2px; }
  .back-details {
    position: absolute; left: 410px; top: 148px;
    color: var(--ink); font-size: 14.5px; line-height: 1.5;
  }
  .back-details .address { margin-bottom: 14px; }
</style>
</head>
<body>
<main class="canvas">

  <section class="card card-front" aria-label="Card front">
    <svg class="card-bands" viewBox="0 0 720 411" aria-hidden="true">
      <polygon points="420,318 720,272 720,290 410,338" fill="var(--teal-dark)"/>
      <polygon points="0,395 395,340 385,358 0,411" fill="var(--teal-light)"/>
    </svg>
    <div class="front-brand">
      <div class="front-name">KORVANE METRICS</div>
      <div class="front-tagline">Measure, Monitor, Save</div>
    </div>
  </section>

  <section class="card card-back" aria-label="Card back">
    <svg class="card-bands" viewBox="0 0 720 411" aria-hidden="true">
      <polygon points="0,330 420,352 410,366 0,344" fill="var(--teal-light)"/>
      <polygon points="432,356 720,372 720,386 422,370" fill="var(--teal-dark)"/>
    </svg>
    <div class="back-brand">KORVANE METRICS</div>
    <div class="back-person">
      <div class="person-name">YOUR NAME</div>
      <div class="person-title">YOUR DESIGNATION</div>
    </div>
    <div class="back-details">
      <p class="address">Abcdefg Hijklm. House,<br>Nopqr Stuvwx, Country.</p>
      <p class="phone">555 - 013 - 2841</p>
      <p class="email">your-email@korvane-example.com</p>
      <p class="web">www.korvane-metrics-example.com</p>
    </div>
  </section>

</main>
</body>
</html>
```